" Fabricamos barrinhas naturais,com intenção de oferecer um produto saudável no mercado.A barrinha pesa 30 gramas, tem um formato semelhante ao da tramelina. São 3 sabores , DAMASCO, AMENDOIM, TÃMARA COM CACAU. "

```html
<!DOCTYPE html>
<html lang="pt-BR">
<head>
<meta charset="UTF-8">
<title>Barra de Cereal – Vellora</title>
<link rel="stylesheet" href="https://fonts.googleapis.com/css2?family=Oswald:wght@400;500&display=swap">
<style>
  :root {
    --magenta: #c4168a;
    --magenta-light: #e13aa6;
    --cream: #f5f0e5;
    --cream-edge: #d8d1c1;
    --orange: #f39218;
    --orange-deep: #e77d0c;
    --brand-green: #4f8a2c;
    --white: #ffffff;
    --page: #ffffff;
  }
  html, body {
    margin: 0;
    width: 1200px;
    height: 1200px;
    overflow: hidden;
    background: var(--page);
  }
  .canvas {
    position: relative;
    width: 1200px;
    height: 1200px;
    font-family: "Oswald", sans-serif;
  }
  .label {
    position: absolute;
    left: 96px;
    top: 108px;
    width: 1008px;
    height: 984px;
    display: flex;
    box-shadow: 0 6px 18px rgba(0,0,0,0.18);
  }
  .side-panel {
    position: relative;
    width: 384px;
    background: linear-gradient(135deg, var(--magenta-light) 0%, var(--magenta) 60%, #b40f7c 100%);
    color: var(--white);
  }
  .product-type {
    position: absolute;
    left: 44px;
    top: 56px;
    margin: 0;
    font-weight: 400;
    font-size: 64px;
    line-height: 1.05;
    letter-spacing: 1px;
  }
  .weight {
    position: absolute;
    left: 44px;
    top: 802px;
    margin: 0;
    font-weight: 400;
    font-size: 76px;
  }
  .side-note {
    position: absolute;
    left: 44px;
    top: 900px;
    width: 300px;
    margin: 0;
    font-family: Arial, sans-serif;
    font-size: 14px;
    line-height: 1.3;
  }
  .main-panel {
    position: relative;
    width: 528px;
    background: radial-gradient(ellipse at 50% 45%, var(--cream) 0%, #ebe5d7 60%, var(--cream-edge) 100%);
    text-align: center;
  }
  .energy {
    position: absolute;
    right: 36px;
    top: 36px;
    margin: 0;
    color: var(--magenta);
    font-size: 30px;
    font-weight: 500;
  }
  .brand {
    position: absolute;
    left: 0;
    right: 0;
    top: 150px;
    display: flex;
    align-items: center;
    justify-content: center;
    gap: 16px;
    color: var(--brand-green);
    font-size: 86px;
    font-weight: 500;
    letter-spacing: 2px;
  }
  .brand-dot {
    width: 34px;
    height: 34px;
    border-radius: 50%;
    background: var(--magenta);
  }
  .tagline {
    position: absolute;
    left: 0;
    right: 0;
    top: 272px;
    margin: 0;
    color: var(--magenta);
    font-size: 19px;
    letter-spacing: 0.5px;
  }
  .flavor {
    position: absolute;
    left: 0;
    right: 0;
    top: 382px;
    margin: 0;
    color: var(--orange);
    font-size: 56px;
    font-weight: 500;
    line-height: 1.1;
    letter-spacing: 1px;
  }
  .claim {
    position: absolute;
    left: 0;
    right: 0;
    top: 584px;
    margin: 0;
    color: var(--orange-deep);
    font-size: 17px;
  }
  .ingredients-photo {
    position: absolute;
    left: 36px;
    top: 660px;
    width: 456px;
    height: 220px;
  }
  .main-note {
    position: absolute;
    left: 0;
    right: 0;
    top: 936px;
    margin: 0;
    color: var(--orange-deep);
    font-family: Arial, sans-serif;
    font-size: 14px;
  }
  .edge-strip {
    width: 96px;
    background: linear-gradient(90deg, var(--orange-deep), var(--orange));
  }
</style>
</head>
<body>
<div class="canvas">
  <div class="label">
    <section class="side-panel">
      <h2 class="product-type">BARRA<br>DE CERAL</h2>
      <p class="weight">30GR</p>
      <p class="side-note">Lorem Ipsum is simply dummy text of the printing and typesetting industry. Lorem ipsum has been the industry's standard</p>
    </section>
    <section class="main-panel">
      <p class="energy">50Kcl</p>
      <div class="brand"><span class="brand-dot"></span><span>Vellora</span></div>
      <p class="tagline">ALIMENTAÇÃO SAUDÁVEL</p>
      <h1 class="flavor">AMENDOIN<br>E DEMASCO</h1>
      <p class="claim">SEM ADIÇÃO DE CONSERVANTES E AÇÚCAR</p>
      <svg class="ingredients-photo" viewBox="0 0 456 220" role="img" aria-label="Foto de damascos secos e amendoins com casca">
        <defs>
          <linearGradient id="fruitTones" x1="0" y1="0" x2="1" y2="0">
            <stop offset="0" stop-color="#f08a1c"/>
            <stop offset="0.5" stop-color="#e9a64a"/>
            <stop offset="1" stop-color="#d9b98a"/>
          </linearGradient>
        </defs>
        <ellipse cx="228" cy="120" rx="220" ry="90" fill="url(#fruitTones)" opacity="0.9"/>
      </svg>
      <p class="main-note">Lorem Ipsum is simply dummy text of the printing and</p>
    </section>
    <div class="edge-strip"></div>
  </div>
</div>
</body>
</html>
```